Business Card Design for ClearPathVitality

We need the new logo on a business card for 3 employees:
Nora Kettering, PhD, Advanced Instructor and Practitioner of SomaLink Integral Medicine (email: nora@clearpathvitality.com)
Ray Holm, Business Manager (email: ray@clearpathvitality.com)
Bea Marlowe, Administrative Assistant (email: bea@helixsense.com)

Target Market(s)

healthcare professionals

Industry/Entity Type

Alternative Medicine

Contact Information for Business Card

Names, titles, emails (names, titles, emails are in project description), phone, address, website, with logo and tagline. See below for address, phone, website: 418 Alder Ln, Bldg 12, Ste 305
Santa Cruz, CA 95060
831-555-2746
www.clearpathvitality.com
Tagline: Roots of Balance, Light of Renewal

Font styles to use
Other font styles liked:
• Gabriela

Colors
00a990
86cfc6
6b449b
b7a5cd
85abd2
abd036

Requirements
Must have
• Colors and style that match the logo design - shades such as blue, green, purple
• Compatible or same font as in the logo
Nice to have
• Nice if it goes with the theme of Nora's last business card - uploaded below
Should not have
• colors or style in conflict with the logo

```html
<!DOCTYPE html>
<html lang="en">
<head>
<meta charset="utf-8">
<title>ClearPathVitality Business Cards</title>
<link rel="stylesheet" href="https://fonts.googleapis.com/css2?family=Gabriela&family=Barlow:wght@400;600&display=swap">
<style>
  :root {
    --page-bg: #3a3a3c;
    --blue-deep: #0d3f86;
    --blue-mid: #1f5fa8;
    --white: #ffffff;
    --green: #48b848;
    --green-light: #8cc63f;
    --teal: #00a990;
    --purple: #4b2a86;
    --purple-soft: #6b449b;
    --navy-text: #1d3f8f;
    --ink: #1e1e24;
  }
  html, body {
    margin: 0;
    padding: 0;
    width: 1200px;
    height: 1000px;
    overflow: hidden;
    background: var(--page-bg);
  }
  .canvas {
    position: relative;
    width: 1200px;
    height: 1000px;
  }
  .card {
    position: absolute;
    border-radius: 22px;
    overflow: hidden;
    box-sizing: border-box;
  }

  /* Front card */
  .card-front {
    left: 500px;
    top: 80px;
    width: 620px;
    height: 354px;
    background: linear-gradient(180deg, var(--blue-mid) 0%, var(--blue-deep) 100%);
  }
  .front-brand {
    position: absolute;
    left: 110px;
    top: 108px;
    display: flex;
    align-items: center;
    gap: 22px;
  }
  .brand-dot {
    width: 92px;
    height: 92px;
    border-radius: 50%;
    background: var(--green);
    flex: none;
  }
  .front-brand .brand-name {
    font-family: "Gabriela", serif;
    font-size: 40px;
    color: var(--white);
    letter-spacing: 0.5px;
  }
  .tagline {
    position: absolute;
    left: 0;
    right: 0;
    top: 268px;
    text-align: center;
    font-family: "Gabriela", serif;
    font-size: 16px;
    letter-spacing: 1.2px;
    text-transform: uppercase;
    color: var(--white);
  }

  /* Back card */
  .card-back {
    left: 80px;
    top: 480px;
    width: 680px;
    height: 388px;
    background: var(--white);
  }
  .back-brand {
    position: absolute;
    left: 30px;
    top: 28px;
    display: flex;
    align-items: center;
    gap: 12px;
  }
  .back-brand .brand-dot {
    width: 58px;
    height: 58px;
  }
  .back-brand .brand-name {
    font-family: "Gabriela", serif;
    font-size: 24px;
    color: var(--purple-soft);
  }
  .person {
    position: absolute;
    left: 32px;
    top: 118px;
  }
  .person-name {
    font-family: "Gabriela", serif;
    font-size: 21px;
    color: var(--navy-text);
    margin: 0 0 4px;
  }
  .person-title {
    font-family: "Gabriela", serif;
    font-size: 11.5px;
    line-height: 1.3;
    text-transform: uppercase;
    color: var(--ink);
    margin: 0;
  }
  .contact {
    position: absolute;
    left: 32px;
    top: 200px;
    font-family: "Barlow", sans-serif;
    font-size: 15px;
    line-height: 1.45;
    color: var(--ink);
  }
  .contact p { margin: 0; }
  .address { margin-bottom: 4px !important; }
  .contact-line {
    display: flex;
    align-items: center;
    gap: 6px;
  }
  .contact-line svg { width: 13px; height: 13px; flex: none; }
  .web-domain { font-weight: 600; color: var(--navy-text); }
  .emblem {
    position: absolute;
    left: 380px;
    top: 44px;
    width: 290px;
    height: 290px;
    border-radius: 50%;
    background: linear-gradient(135deg, var(--green-light) 0%, var(--teal) 50%, var(--purple) 100%);
    display: flex;
    align-items: center;
    justify-content: center;
  }
  .emblem .brand-name {
    font-family: "Gabriela", serif;
    font-size: 24px;
    color: var(--white);
  }
</style>
</head>
<body>
<main class="canvas">

  <section class="card card-front" aria-label="Business card front">
    <div class="front-brand">
      <span class="brand-dot"></span>
      <span class="brand-name">ClearPathVitality</span>
    </div>
    <p class="tagline">Roots of Balance, Light of Renewal</p>
  </section>

  <section class="card card-back" aria-label="Business card back">
    <div class="back-brand">
      <span class="brand-dot"></span>
      <span class="brand-name">ClearPathVitality</span>
    </div>

    <div class="person">
      <h1 class="person-name">Nora Kettering</h1>
      <p class="person-title">PhD, Advanced Instructor<br>and Practitioner</p>
    </div>

    <div class="contact">
      <p class="address">418 Alder Ln, Bldg 12,<br>Ste 305 Santa Cruz, CA 95060</p>
      <p class="contact-line">
        <svg viewBox="0 0 16 16" aria-hidden="true"><path d="M4 1.5l2.5 3-1.5 1.6c.8 1.9 2.3 3.4 4.2 4.2L10.8 8.8l3 2.5-1.4 2.6C7.2 14 2 8.8 1.4 3.2z" fill="var(--green)"/></svg>
        831-555-2746
      </p>
      <p class="contact-line">
        <svg viewBox="0 0 16 16" aria-hidden="true"><rect x="1" y="3" width="14" height="10" rx="1" fill="var(--green)"/><path d="M1.5 3.8 8 9l6.5-5.2" stroke="#fff" stroke-width="1.3" fill="none"/></svg>
        nora@clearpathvitality.com
      </p>
      <p class="contact-line">
        <svg viewBox="0 0 16 16" aria-hidden="true"><circle cx="8" cy="8" r="6.5" fill="none" stroke="var(--green)" stroke-width="1.5"/><path d="M1.5 8h13M8 1.5c-3 3.5-3 9.5 0 13M8 1.5c3 3.5 3 9.5 0 13" stroke="var(--green)" stroke-width="1.2" fill="none"/></svg>
        www.<span class="web-domain">clearpathvitality</span>.com
      </p>
    </div>

    <div class="emblem">
      <span class="brand-name">ClearPathVitality</span>
    </div>
  </section>

</main>
</body>
</html>
```